Business Card Design

I am a new realtor. To stand out from the other 25 realtors in my firm I need a card that will stand out. I am the youngest realtor here, so I want something to reflect that. Something different, as opposed to the same old traditional, boring cards everyone else has. It of course needs to have my picture which I will download for you ( I included a black and white option as well as color. Either are fine) and you can crop it or do whatever you need to make it look the best. Our company colors are red and white. These don't have to be the only colors on the card, but the red especially needs to be a focal color. I like a clean, stream-line look while still eye-catching. Not over the top busy.
While I do have to provide the company logo, I am a contractor. Therefore, I want the focus on me and my information.
Industry/Entity Type
Realtor
Contact Information for Business Card
Marisa Quillon
Realtor (this needs the realtor logo which has the R in the circle at the end)
(office)555.318.4406
(cell) 555.892.6035
Mquillon@brv-homegroup.example
It will also need our company logo which I will download and send
Requirements
Nice to have
- I like the look of the foil or metallic. However, this is definitely not a requirement

```html
<!DOCTYPE html>
<html lang="en">
<head>
<meta charset="utf-8">
<title>Realtor Business Card – Front and Back</title>
<link rel="stylesheet" href="https://fonts.googleapis.com/css2?family=Fira+Sans+Condensed:wght@400;600&family=Fira+Sans+Extra+Condensed:wght@300&display=swap">
<style>
  :root {
    --page-bg: #ffffff;
    --card-bg: #ffffff;
    --brand-red: #d9232a;
    --text-grey: #5e5e60;
    --label-grey: #a9a9ab;
    --photo-light: #f2f2f3;
    --photo-mid: #c9c9cb;
    --photo-dark: #5a5a5c;
    --card-shadow: rgba(0, 0, 0, 0.38);
  }
  * { margin: 0; padding: 0; box-sizing: border-box; }
  html, body {
    width: 1200px;
    height: 1000px;
    overflow: hidden;
    background: var(--page-bg);
  }
  .sheet {
    position: relative;
    width: 1200px;
    height: 1000px;
    font-family: "Fira Sans Condensed", "Arial Narrow", sans-serif;
  }
  .card {
    position: absolute;
    background: var(--card-bg);
    box-shadow: 3px 4px 6px var(--card-shadow);
    overflow: hidden;
  }
  .card--front {
    left: 47px; top: 44px;
    width: 743px; height: 433px;
    background: linear-gradient(150deg, #e9e9ea 0%, #f7f7f8 45%, #ffffff 70%, #f1f1f2 100%);
  }
  .card--back {
    left: 409px; top: 522px;
    width: 753px; height: 441px;
  }
  .portrait {
    position: absolute;
    left: 0; top: 0;
    width: 330px; height: 433px;
    background:
      radial-gradient(ellipse 120px 180px at 160px 240px, var(--photo-dark) 0%, rgba(90,90,92,0.55) 55%, rgba(90,90,92,0) 100%),
      radial-gradient(ellipse 150px 120px at 170px 390px, #ebebec 0%, rgba(235,235,236,0) 100%),
      linear-gradient(90deg, var(--photo-light) 0%, var(--photo-mid) 50%, var(--photo-light) 100%);
    -webkit-mask-image: linear-gradient(90deg, #000 75%, transparent 100%);
            mask-image: linear-gradient(90deg, #000 75%, transparent 100%);
  }
  .contact {
    position: absolute;
    left: 395px; top: 190px;
    color: var(--text-grey);
    list-style: none;
  }
  .contact__name {
    color: var(--brand-red);
    font-weight: 600;
    font-size: 25px;
    line-height: 30px;
    margin-bottom: 15px;
  }
  .contact__line {
    font-size: 23px;
    line-height: 30px;
    margin-bottom: 15.5px;
    white-space: nowrap;
  }
  .contact__line sup { font-size: 14px; }
  .contact__tag { font-size: 18px; }
  .side-label {
    position: absolute;
    font-family: "Fira Sans Extra Condensed", "Arial Narrow", sans-serif;
    font-weight: 300;
    font-size: 30px;
    letter-spacing: 3px;
    color: var(--label-grey);
  }
  .side-label--front { left: 137px; top: 497px; }
  .side-label--back { left: 970px; top: 461px; }
  .brokerage {
    position: absolute;
    left: 0; right: 0; top: 0; bottom: 0;
    display: flex;
    align-items: center;
    justify-content: center;
    gap: 18px;
  }
  .brokerage__mark {
    width: 34px; height: 34px;
    background: var(--brand-red);
  }
  .brokerage__name {
    color: var(--brand-red);
    font-weight: 600;
    font-size: 46px;
    letter-spacing: 0.5px;
  }
</style>
</head>
<body>
  <main class="sheet">
    <section class="card card--front" aria-label="Card front">
      <div class="portrait" role="img" aria-label="Black and white portrait photograph of the realtor"></div>
      <ul class="contact">
        <li class="contact__name">Marisa Quillon</li>
        <li class="contact__line">Realtor<sup>®</sup></li>
        <li class="contact__line">555.318.4406 <span class="contact__tag">office</span></li>
        <li class="contact__line">555.892.6035 <span class="contact__tag">cell</span></li>
        <li class="contact__line">Mquillon@brv-homegroup.example</li>
      </ul>
    </section>
    <p class="side-label side-label--front">FRONT</p>

    <p class="side-label side-label--back">BACK</p>
    <section class="card card--back" aria-label="Card back">
      <div class="brokerage">
        <span class="brokerage__mark" aria-hidden="true"></span>
        <span class="brokerage__name">Halden Marsh &amp; Company</span>
      </div>
    </section>
  </main>
</body>
</html>
```